The Willow Gate: Steady Horizon

Please use the attached images as a reference and as inspiration for this contest. Please note, these images are google searched and belong to someone else.
This project is for our church.
We have a new Sermon Series launching and we want to be able to promote it and manipulate the size of the project via Facebook Cover Art, CD Labels, T-Shirts, Banners, etc.
Requesting a HD 1080 X 920 pixels.
Need an editable PSD file from the winner of the contest.
The title of the project is: Steady Horizon.
The idea behind this project is bringing things in life into focus to help our congregation be intentional about focusing on making positive changes to major areas of life.
When we think of this - we think of a camera brining something into focus to take that perfect shot, or as one of the attached images show blurry images coming into focus.
Keywords that can be used in the design are: Faith, Family, Finances, and Fitness.
Just because it is for a church does NOT mean we need it to look like its for a church. In fact, we desire the design to be compelling to someone who has never stepped foot into a church building. Avoid a "church" look.
Good Luck!
Target Market(s)
Everyone
Industry/Entity Type
House
Requirements
Must have
- Bringing "things" into focus.
- Please read description for more details
Should not have
- A church look

```html
<!DOCTYPE html>
<html lang="en">
<head>
<meta charset="utf-8">
<title>Steady Horizon – Sermon Series Cover</title>
<link href="https://fonts.googleapis.com/css2?family=Poppins:wght@700;800&display=swap" rel="stylesheet">
<style>
  :root {
    --backdrop: #5d5e68;
    --sky-top: #d6e2f0;
    --sky-low: #e8eef4;
    --sea-far: #7fa9bc;
    --sea-near: #a9c6cf;
    --surf: #e4e8ea;
    --sand-light: #ddd6ca;
    --sand-deep: #c7b79e;
    --type: #ffffff;
  }
  * { margin: 0; padding: 0; box-sizing: border-box; }
  html, body {
    width: 1200px;
    height: 841px;
    overflow: hidden;
    background: var(--backdrop);
  }
  .cover {
    position: absolute;
    left: 250px;
    top: 70px;
    width: 700px;
    height: 700px;
    overflow: hidden;
  }
  .cover-photo {
    position: absolute;
    inset: 0;
    background: linear-gradient(
      to bottom,
      var(--sky-top) 0%,
      var(--sky-low) 48%,
      var(--sea-far) 51%,
      var(--sea-near) 58%,
      var(--surf) 62%,
      var(--sand-light) 75%,
      var(--sand-deep) 100%
    );
  }
  .title {
    position: absolute;
    left: 0;
    right: 0;
    text-align: center;
    color: var(--type);
    font-family: "Poppins", sans-serif;
    text-transform: uppercase;
  }
  .title-kicker {
    top: 36px;
    font-size: 31px;
    font-weight: 700;
    letter-spacing: 2px;
    line-height: 1;
  }
  .title-main {
    top: 82px;
    font-size: 122px;
    font-weight: 800;
    letter-spacing: 4px;
    line-height: 1;
  }
  .series-label {
    position: absolute;
    left: 0;
    right: 0;
    bottom: 10px;
    text-align: center;
    color: var(--type);
    font-family: "Poppins", sans-serif;
    font-weight: 700;
    font-size: 10px;
    letter-spacing: 1px;
    text-transform: uppercase;
  }
</style>
</head>
<body>
  <main class="cover">
    <div class="cover-photo" role="img" aria-label="Photo of a child seen from behind, arms spread wide, standing barefoot on a motion-blurred beach facing the sea under a pale sky"></div>
    <p class="title title-kicker">Steady</p>
    <h1 class="title title-main">Horizon</h1>
    <p class="series-label">Sermon Serie</p>
  </main>
</body>
</html>
```